Brenmoor Estates Website and Logo Design

We need a new logo and website designed for 'Brenmoor Estates Ltd', which is a well established Guernsey property holding company founded in 1934.

The company does not currently have a website. The new website should be similar in style and layout to https://www.quillfenhouse.example/.

Target Market(s)

Industry, Media, Tenants

Industry/Entity Type

Property Management

Logo Text

BEL OR Brenmoor Estates Ltd OR BE

Coding

Coded - Design and coding required

Number of Pages Required

4 page

Font styles to use
Other font styles liked:
• Helvetica

Requirements
Must have
• The logo laying over the picture (like https://www.quillfenhouse.example/).
• Big pictures on homepage (like https://www.quillfenhouse.example/)

```html
<!DOCTYPE html>
<html lang="en">
<head>
<meta charset="utf-8">
<title>Brenmoor Estates Ltd</title>
<link rel="stylesheet" href="https://fonts.googleapis.com/css2?family=Poppins:wght@400;500;600;700&family=Open+Sans:wght@400;600;700&display=swap">
<style>
:root{
  --plum:#341452;
  --plum-deep:#2a0f44;
  --violet:#a95ce6;
  --ink:#222;
  --muted:#444;
  --white:#fff;
  --rule:#d9cfe6;
}
*{box-sizing:border-box;margin:0;padding:0}
html,body{width:1200px;height:2752px;overflow:hidden;background:var(--white)}
body{position:relative;font-family:"Open Sans",Helvetica,Arial,sans-serif;color:var(--ink)}
.abs{position:absolute}

/* hero */
.hero{left:0;top:0;width:1200px;height:600px;
  background:linear-gradient(180deg,#3f7ed6 0%,#8fb7e6 16%,#c9c2b4 24%,#8e8a7c 33%,#4d6f78 42%,#2c6e86 60%,#1f5f7a 80%,#174b62 100%)}
.topbar{left:339px;top:0;width:520px;height:22px;background:var(--plum);border-radius:0 0 14px 14px;
  display:flex;justify-content:center;align-items:center;gap:26px;color:var(--white);font-size:9px;font-weight:600}
.topbar span{display:flex;align-items:center;gap:5px}
.brand{left:132px;top:30px;display:flex;align-items:center;gap:8px}
.brand-mark{width:26px;height:26px;background:var(--violet)}
.brand-name{font-family:"Poppins",Helvetica,sans-serif;font-weight:600;font-size:15px;color:var(--plum);line-height:1}
.nav{right:130px;top:40px;display:flex;gap:26px;font-family:"Poppins",Helvetica,sans-serif;font-size:14px;color:var(--white)}
.nav a{color:inherit;text-decoration:none}
.nav .active{color:#2b1a5c}
.nav-rule{left:132px;top:80px;width:938px;height:2px;background:rgba(255,255,255,.85)}
.slider-tab{left:495px;top:556px;width:213px;height:44px}
.dots{left:544px;top:570px;display:flex;gap:10px}
.dots i{display:block;width:14px;height:14px;border-radius:50%;background:var(--plum)}
.dots i:first-child{background:var(--white);border:3px solid var(--plum)}

/* headings */
.section-title{left:0;width:1200px;text-align:center;font-family:"Poppins",Helvetica,sans-serif;font-weight:600;font-size:32px;color:var(--plum)}
.btn{display:flex;align-items:center;justify-content:center;font-family:"Poppins",Helvetica,sans-serif;font-weight:600;font-size:16px;letter-spacing:.3px}
.btn-outline{border:2px solid var(--plum);color:var(--plum);background:var(--white)}
.btn-solid{background:var(--plum);color:var(--white)}

/* about */
.about-col{top:714px;width:408px;font-size:13.5px;line-height:20px;color:var(--muted);text-align:justify;text-align-last:center}

/* projects */
.projects{left:0;top:952px;width:1200px;height:481px;display:grid;grid-template-columns:repeat(4,300px);grid-template-rows:240px 241px}
.tile{position:relative;overflow:hidden}
.tile .corner{position:absolute;right:0;bottom:0;width:106px;height:106px;background:var(--violet);clip-path:polygon(100% 0,100% 100%,0 100%)}
.tile .corner svg{position:absolute;right:16px;bottom:16px}
.tile-intro{background:var(--plum)}
.tile-intro .flag{position:absolute;left:0;top:0;width:110px;height:110px;background:var(--violet);clip-path:polygon(0 0,100% 0,0 100%)}
.tile-intro .flag svg{position:absolute;left:20px;top:30px}
.tile-intro h3{position:absolute;left:138px;top:50px;font-family:"Poppins",Helvetica,sans-serif;font-weight:400;font-size:23px;color:var(--white)}
.tile-intro p{position:absolute;left:138px;top:92px;width:150px;font-size:11.5px;line-height:17px;color:var(--white);text-align:justify}
.tile-intro .more{position:absolute;left:138px;top:178px;font-size:10px;color:var(--white);font-weight:600}
.p1{background:linear-gradient(135deg,#b7a9f0 0%,#6d63d8 45%,#2b3aa8 100%)}
.p2{background:linear-gradient(160deg,#2b1b66 0%,#4a3fb0 50%,#8f7fe0 100%)}
.p3{background:linear-gradient(150deg,#1a3b8c 0%,#5a6bb0 50%,#2d2a6e 100%)}
.p4{background:linear-gradient(140deg,#3a76d8 0%,#1e4aa0 55%,#0e2a68 100%)}
.p5{background:linear-gradient(120deg,#6f9be6 0%,#e6eef8 45%,#2a2a48 75%,#d8e4f4 100%)}
.p6{background:linear-gradient(180deg,#4a5aa0 0%,#9aa4c8 50%,#3a3f70 100%)}
.p7{background:linear-gradient(170deg,#5a4680 0%,#8a8ad0 50%,#2a2458 100%)}

/* blog */
.post{top:1617px;width:292px}
.post .date{position:absolute;left:0;top:0;width:136px;height:58px;background:var(--plum);clip-path:polygon(0 0,100% 0,72% 100%,0 100%);
  color:var(--white);font-family:"Poppins",Helvetica,sans-serif;font-weight:600;padding:6px 0 0 26px;line-height:20px;z-index:2}
.post .date small{font-size:16px;display:block}
.post .date b{font-size:21px}
.post .photo{position:absolute;left:0;top:22px;width:292px;height:306px}
.post h4{position:absolute;left:0;top:344px;font-family:"Poppins",Helvetica,sans-serif;font-weight:600;font-size:13.5px;color:var(--plum)}
.post p{position:absolute;left:0;top:364px;width:292px;height:60px;overflow:hidden;font-size:11.5px;line-height:18px;color:var(--muted);text-align:justify}
.post .comments{position:absolute;left:0;top:444px;display:flex;align-items:center;gap:6px;font-size:11px;font-weight:700;color:var(--plum)}
.b1{background:linear-gradient(135deg,#4d8fdc 0%,#d9e6f4 40%,#1c2030 70%,#9fb8dc 100%)}
.b2{background:linear-gradient(160deg,#0e6f7a 0%,#2f5660 45%,#1a2a34 100%)}
.b3{background:linear-gradient(160deg,#6b6590 0%,#4b4da8 45%,#2a2848 100%)}

/* contact */
.map{left:0;top:2207px;width:600px;height:545px;background:linear-gradient(135deg,#eeece4 0%,#f3efd2 40%,#e6e6dc 70%,#d9e4ea 100%)}
.contact{left:600px;top:2207px;width:600px;height:445px;background:var(--plum)}
.contact h2{position:absolute;left:35px;top:54px;font-family:"Poppins",Helvetica,sans-serif;font-weight:500;font-size:32px;color:var(--white)}
.field{position:absolute;left:35px;width:435px;border-bottom:1px solid var(--rule);color:var(--white);font-size:11px;padding:0 0 8px 11px;letter-spacing:.3px}
.send{position:absolute;left:35px;top:351px;width:136px;height:30px;background:var(--white);color:var(--plum)}
.social{left:600px;top:2652px;width:600px;height:60px;background:var(--white);display:flex;align-items:center;gap:38px;padding-left:37px}
.social i{display:block;width:12px;height:12px;border-radius:50%;background:var(--plum)}
.footer{left:600px;top:2712px;width:600px;height:40px;background:var(--plum);color:var(--white);font-size:11px;font-weight:600;display:flex;align-items:center;padding-left:35px}
</style>
</head>
<body>

<section class="hero abs" role="img" aria-label="Photograph of a harbour town with moored boats and waterfront houses"></section>
<div class="topbar abs">
  <span><svg width="8" height="10" viewBox="0 0 8 10"><path d="M4 0a3.5 3.5 0 0 0-3.5 3.5C.5 6 4 10 4 10s3.5-4 3.5-6.5A3.5 3.5 0 0 0 4 0zm0 5a1.4 1.4 0 1 1 0-2.8A1.4 1.4 0 0 1 4 5z" fill="#fff"/></svg>Lorem Ipsum Dolor, Sit Amet, Elit-123456</span>
  <span><svg width="10" height="8" viewBox="0 0 10 8"><rect x=".5" y=".5" width="9" height="7" fill="none" stroke="#fff"/><path d="M.5.5 5 4.5 9.5.5" fill="none" stroke="#fff"/></svg>info@brenmoorestates.example</span>
  <span><svg width="9" height="9" viewBox="0 0 9 9"><path d="M2 0 3.5 2.5 2.5 3.5A6 6 0 0 0 5.5 6.5l1-1L9 7 8 9C4 9 0 5 0 1z" fill="#fff"/></svg>+ 0000000000</span>
</div>
<div class="brand abs"><span class="brand-mark"></span><span class="brand-name">Brenmoor Estates Ltd</span></div>
<nav class="nav abs"><a class="active">HOME</a><a>ABOUT US</a><a>PROJECTS</a><a>BLOG</a><a>CONTACT US</a></nav>
<div class="nav-rule abs"></div>
<svg class="slider-tab abs" viewBox="0 0 213 44"><polygon points="22,0 191,0 213,44 0,44" fill="#fff"/></svg>
<div class="dots abs"><i></i><i></i><i></i><i></i><i></i></div>

<h2 class="section-title abs" style="top:654px">ABOUT US</h2>
<p class="about-col abs" style="left:191px">Lorem ipsum dolor sit amet, consectetur adipiscing elit. Sed suscipit consequat quam ut aliquet. Cum sociis natoque penatibus et magnis dis parturient montes, nascetur ridiculus mus.</p>
<p class="about-col abs" style="left:607px">Lorem ipsum dolor sit amet, consectetur adipiscing elit. Sed suscipit consequat quam ut aliquet. Cum sociis natoque penatibus et magnis dis parturient montes, nascetur ridiculus mus.</p>
<div class="btn btn-outline abs" style="left:532px;top:802px;width:134px;height:33px">VIEW MORE</div>

<h2 class="section-title abs" style="top:887px">OUR PROJECTS</h2>
<section class="projects abs">
  <div class="tile tile-intro">
    <div class="flag"><svg width="30" height="4"><rect width="30" height="3" fill="#fff"/></svg></div>
    <h3>LOREM IPSUM</h3>
    <p>Lorem ipsum dolor sit amet, consectetur adipiscing elit. Sed suscipit consequat quam ut aliquet.</p>
    <span class="more">Read More ›</span>
  </div>
  <div class="tile p1" role="img" aria-label="Glass office tower seen from below"><span class="corner"><svg width="40" height="40"><path d="M20 2v36M2 20h36" stroke="#fff" stroke-width="4"/></svg></span></div>
  <div class="tile p2" role="img" aria-label="Curved modern office building"><span class="corner"><svg width="40" height="40"><path d="M20 2v36M2 20h36" stroke="#fff" stroke-width="4"/></svg></span></div>
  <div class="tile p3" role="img" aria-label="Tall glass tower against a blue sky"><span class="corner"><svg width="40" height="40"><path d="M20 2v36M2 20h36" stroke="#fff" stroke-width="4"/></svg></span></div>
  <div class="tile p4" role="img" aria-label="Blue glass building facade"><span class="corner"><svg width="40" height="40"><path d="M20 2v36M2 20h36" stroke="#fff" stroke-width="4"/></svg></span></div>
  <div class="tile p5" role="img" aria-label="Pointed building edge against clouds"><span class="corner"><svg width="40" height="40"><path d="M20 2v36M2 20h36" stroke="#fff" stroke-width="4"/></svg></span></div>
  <div class="tile p6" role="img" aria-label="Group of city skyscrapers"><span class="corner"><svg width="40" height="40"><path d="M20 2v36M2 20h36" stroke="#fff" stroke-width="4"/></svg></span></div>
  <div class="tile p7" role="img" aria-label="Glass tower at dusk"><span class="corner"><svg width="40" height="40"><path d="M20 2v36M2 20h36" stroke="#fff" stroke-width="4"/></svg></span></div>
</section>
<div class="btn btn-solid abs" style="left:532px;top:1464px;width:134px;height:33px">VIEW MORE</div>

<h2 class="section-title abs" style="top:1552px">OUR BLOG</h2>
<article class="post abs" style="left:132px">
  <div class="date"><small>20th Dec</small><b>2016</b></div>
  <div class="photo b1" role="img" aria-label="Angular building against a cloudy sky"></div>
  <h4>LOREM IPSUM</h4>
  <p>Lorem ipsum dolor sit amet, consectetur adipiscing elit. Quisque at volutpat lorem, semper ornare sapien. Nam elementum velit et odio rhoncus ullamcorper.Lorem ipsum dolor sit amet, consectetur adipiscing elit.</p>
  <span class="comments"><svg width="20" height="14" viewBox="0 0 20 14"><path d="M1 1h11v7H5L2 11V8H1z" fill="none" stroke="#341452" stroke-width="1.6"/><path d="M14 4h5v7h-1v2l-3-2H8V9" fill="none" stroke="#341452" stroke-width="1.6"/></svg>6 Comments</span>
</article>
<article class="post abs" style="left:454px">
  <div class="date"><small>21st Dec</small><b>2016</b></div>
  <div class="photo b2" role="img" aria-label="Dark office tower seen from below"></div>
  <h4>LOREM IPSUM</h4>
  <p>Lorem ipsum dolor sit amet, consectetur adipiscing elit. Quisque at volutpat lorem, semper ornare sapien. Nam elementum velit et odio rhoncus ullamcorper.Lorem ipsum dolor sit amet, consectetur adipiscing elit.</p>
  <span class="comments"><svg width="20" height="14" viewBox="0 0 20 14"><path d="M1 1h11v7H5L2 11V8H1z" fill="none" stroke="#341452" stroke-width="1.6"/><path d="M14 4h5v7h-1v2l-3-2H8V9" fill="none" stroke="#341452" stroke-width="1.6"/></svg>7 Comments</span>
</article>
<article class="post abs" style="left:776px">
  <div class="date"><small>22nd Dec</small><b>2016</b></div>
  <div class="photo b3" role="img" aria-label="Glass tower at dusk"></div>
  <h4>LOREM IPSUM</h4>
  <p>Lorem ipsum dolor sit amet, consectetur adipiscing elit. Quisque at volutpat lorem, semper ornare sapien. Nam elementum velit et odio rhoncus ullamcorper.Lorem ipsum dolor sit amet, consectetur adipiscing elit.</p>
  <span class="comments"><svg width="20" height="14" viewBox="0 0 20 14"><path d="M1 1h11v7H5L2 11V8H1z" fill="none" stroke="#341452" stroke-width="1.6"/><path d="M14 4h5v7h-1v2l-3-2H8V9" fill="none" stroke="#341452" stroke-width="1.6"/></svg>8Comments</span>
</article>
<div class="btn btn-outline abs" style="left:532px;top:2111px;width:134px;height:31px">VIEW MORE</div>

<div class="map abs" role="img" aria-label="Street map showing the office location"></div>
<section class="contact abs">
  <h2>CONTACT US</h2>
  <div class="field" style="top:131px">NAME</div>
  <div class="field" style="top:176px">E-MAIL ADDRESS</div>
  <div class="field" style="top:221px;height:95px">MESSAGE</div>
  <div class="btn send">SEND NOW</div>
</section>
<div class="social abs"><i></i><i></i><i></i><i></i><i></i></div>
<footer class="footer abs">Copyright @ 2016 BRENMOOR ESTATES LTD. All Rights Reserved.</footer>

</body>
</html>
```